Easter & Summer School Dance Camps

I need two flyers one for Easter camps and one for summer school
We are a performing arts and dance academy

I want a double sided flyers one side summer school one side easter camp
Updates

Please make these flyers appeal to young dancers and performers - eye catching up to date Added Tuesday, March 1, 2016

Target Market(s)

Young children and teenagers

Industry/Entity Type

School

Font styles to use
Serif
Sans Serif

Requirements
Must have
• bright colourful

```html
<!DOCTYPE html>
<html lang="en">
<head>
<meta charset="utf-8">
<title>Fun, Fresh &amp; Funky – Easter Dance Camps</title>
<link rel="stylesheet" href="https://fonts.googleapis.com/css2?family=Ubuntu:wght@500;700&family=Quicksand:wght@500;700&display=swap">
<style>
  :root{
    --page:#e9e9e9;
    --ink-dark:#2a2a2a;
    --paper-light:#f1f3f3;
    --yellow:#f9c25c;
    --yellow-deep:#e8b23a;
    --orange:#ee5a34;
    --orange-head:#f7a823;
    --orange-head-light:#ee6c1b;
    --pink:#f36db0;
    --green:#7ac36a;
    --green-deep:#3aa94f;
    --blue:#1f86cf;
    --blue-deep:#1a73b8;
    --white:#ffffff;
    --text-dark:#1d1d1d;
  }
  html,body{margin:0;height:100%;overflow:hidden}
  body{
    width:1200px;height:900px;background:var(--page);
    display:flex;align-items:center;justify-content:center;gap:40px;
  }
  .flyer{width:540px;height:764px;display:block;box-shadow:0 6px 18px rgba(0,0,0,.18)}
  .headline{font-family:"Ubuntu",sans-serif;font-weight:700}
  .body-text{font-family:"Quicksand",sans-serif;font-weight:700}
  .flyer--dark .bg{fill:var(--ink-dark)}
  .flyer--light .bg{fill:var(--paper-light)}
  .flyer--dark .headline-top{fill:var(--white)}
  .flyer--dark .headline-main{fill:var(--orange-head)}
  .flyer--light .headline-top,.flyer--light .headline-main{fill:var(--orange-head-light)}
  .flyer--dark .tagline{fill:var(--white)}
  .flyer--light .tagline{fill:var(--text-dark)}
  .tri-yellow{fill:var(--yellow)}
  .tri-yellow-deep{fill:var(--yellow-deep)}
  .tri-orange{fill:var(--orange)}
  .tri-pink{fill:var(--pink)}
  .tri-green{fill:var(--green)}
  .tri-green-deep{fill:var(--green-deep)}
  .tri-blue{fill:var(--blue)}
  .edge{stroke:var(--white);stroke-width:4}
  .inner-line{fill:none;stroke:var(--text-dark);stroke-width:1;stroke-dasharray:3 3;opacity:.5}
  .venue-text,.price-text{fill:var(--white)}
  .workshop-text,.brand-name,.brand-sub{fill:var(--text-dark)}
  .booking-box{fill:var(--yellow)}
  .flyer--light .booking-box{fill:var(--white)}
  .booking-label{fill:var(--text-dark)}
  .flyer--dark .booking-phone,.flyer--dark .booking-email{fill:var(--blue-deep)}
  .flyer--light .booking-phone,.flyer--light .booking-email{fill:var(--blue)}
  .dash{stroke:var(--white);stroke-width:1;stroke-dasharray:3 3}
</style>
</head>
<body>

<svg class="flyer flyer--dark" viewBox="0 0 540 764" xmlns="http://www.w3.org/2000/svg">
  <defs>
    <linearGradient id="dancersWhite" x1="0" y1="0" x2="1" y2="1">
      <stop offset="0" stop-color="#ffffff"/>
      <stop offset="0.6" stop-color="#ffffff"/>
      <stop offset="1" stop-color="#f9c25c"/>
    </linearGradient>
  </defs>
  <rect class="bg" width="540" height="764"/>

  <text class="headline headline-top" x="28" y="72" font-size="50">FUN, FRESH &amp;</text>
  <text class="headline headline-main" x="28" y="128" font-size="58">FUNKY</text>
  <text class="body-text tagline" x="30" y="160" font-size="15">Easter dance camps mixed together with</text>
  <text class="body-text tagline" x="30" y="180" font-size="15">a little musical theatre!</text>

  <polygon class="tri-green" points="468,150 540,150 540,228"/>
  <polygon class="tri-pink" points="540,228 540,312 452,312"/>

  <polygon class="tri-pink" points="0,560 112,560 0,676"/>
  <polygon class="tri-green" points="112,600 205,712 58,712"/>
  <polygon class="tri-yellow-deep" points="0,648 205,764 0,764"/>
  <polygon class="tri-green" points="420,764 540,764 540,632"/>
  <polygon class="tri-pink" points="540,600 540,700 505,650"/>
  <polygon class="tri-orange" points="540,560 540,630 500,596"/>

  <rect x="60" y="205" width="300" height="559" rx="140" fill="url(#dancersWhite)" role="img" aria-label="Silhouettes of two young dancers in mid-move"/>

  <polygon class="tri-blue edge" points="380,270 540,270 540,520"/>
  <g class="body-text venue-text" text-anchor="end">
    <text x="528" y="302" font-size="16">VENUE</text>
    <text x="528" y="322" font-size="13">The Parish Hall</text>
    <text x="528" y="340" font-size="13">of St Aldric</text>
    <text x="528" y="358" font-size="13">Elm</text>
    <text x="528" y="376" font-size="13">Green</text>
    <text x="528" y="394" font-size="13">KT9 0ZZ</text>
  </g>

  <polygon class="tri-orange edge" points="445,358 527,497 363,497"/>
  <g class="body-text price-text" text-anchor="middle">
    <text x="445" y="428" font-size="15">30</text>
    <text x="445" y="445" font-size="14">per day</text>
    <line class="dash" x1="415" y1="454" x2="475" y2="454"/>
    <text x="445" y="471" font-size="15">55</text>
    <text x="445" y="488" font-size="14">for both</text>
  </g>

  <polygon class="tri-yellow edge" points="200,502 540,502 370,764"/>
  <polygon class="inner-line" points="225,514 515,514 370,738"/>
  <g text-anchor="middle">
    <circle cx="302" cy="561" r="5" fill="var(--pink)"/>
    <text class="body-text brand-name" x="375" y="570" font-size="28">Brightstep</text>
    <text class="body-text brand-sub" x="372" y="588" font-size="8">ACADEMY OF DANCE AND PERFORMING ARTS</text>
    <text class="body-text workshop-text" x="370" y="625" font-size="13">WEST END WORKSHOP</text>
    <text class="body-text workshop-text" x="370" y="643" font-size="12">Tuesday</text>
    <text class="body-text workshop-text" x="370" y="660" font-size="12">5 &amp; 6 April 2016</text>
    <text class="body-text workshop-text" x="370" y="677" font-size="12">8 – 16 years</text>
    <text class="body-text workshop-text" x="370" y="694" font-size="12">1-4pm</text>
  </g>

  <rect class="booking-box" x="56" y="690" width="176" height="74"/>
  <text class="body-text booking-label" x="144" y="708" font-size="12" text-anchor="middle">FOR BOOKING</text>
  <rect x="68" y="716" width="9" height="15" rx="2" fill="none" stroke="var(--blue-deep)" stroke-width="2"/>
  <text class="body-text booking-phone" x="82" y="731" font-size="19">07700 900123</text>
  <text class="body-text booking-email" x="68" y="750" font-size="10">✉ hello@brightstepdance.co</text>
</svg>

<svg class="flyer flyer--light" viewBox="0 0 540 764" xmlns="http://www.w3.org/2000/svg">
  <defs>
    <linearGradient id="dancersBlue" x1="0" y1="0" x2="1" y2="1">
      <stop offset="0" stop-color="#1f86cf"/>
      <stop offset="0.65" stop-color="#1f86cf"/>
      <stop offset="1" stop-color="#f9c25c"/>
    </linearGradient>
  </defs>
  <rect class="bg" width="540" height="764"/>

  <text class="headline headline-top" x="28" y="72" font-size="50">FUN, FRESH &amp;</text>
  <text class="headline headline-main" x="28" y="128" font-size="58">FUNKY</text>
  <text class="body-text tagline" x="30" y="160" font-size="15">Easter dance camps mixed together with</text>
  <text class="body-text tagline" x="30" y="180" font-size="15">a little musical theatre!</text>

  <polygon class="tri-green" points="468,0 540,0 540,60"/>
  <polygon class="tri-pink" points="540,80 540,200 480,200"/>

  <polygon class="tri-pink" points="0,560 112,560 0,676"/>
  <polygon class="tri-green" points="112,600 205,712 58,712"/>
  <polygon class="tri-yellow-deep" points="0,648 205,764 0,764"/>
  <polygon class="tri-green" points="420,764 540,764 540,632"/>
  <polygon class="tri-pink" points="540,600 540,700 505,650"/>
  <polygon class="tri-orange" points="540,560 540,630 500,596"/>

  <rect x="60" y="205" width="300" height="559" rx="140" fill="url(#dancersBlue)" role="img" aria-label="Silhouettes of two young dancers in mid-move"/>

  <polygon class="tri-blue edge" points="380,270 540,270 540,520"/>
  <g class="body-text venue-text" text-anchor="end">
    <text x="528" y="302" font-size="16">VENUE</text>
    <text x="528" y="322" font-size="13">The Parish Hall</text>
    <text x="528" y="340" font-size="13">of St Aldric</text>
    <text x="528" y="358" font-size="13">Elm</text>
    <text x="528" y="376" font-size="13">Green</text>
    <text x="528" y="394" font-size="13">KT9 0ZZ</text>
  </g>

  <polygon class="tri-orange edge" points="445,358 527,497 363,497"/>
  <g class="body-text price-text" text-anchor="middle">
    <text x="445" y="428" font-size="15">30</text>
    <text x="445" y="445" font-size="14">per day</text>
    <line class="dash" x1="415" y1="454" x2="475" y2="454"/>
    <text x="445" y="471" font-size="15">55</text>
    <text x="445" y="488" font-size="14">for both</text>
  </g>

  <polygon class="tri-yellow edge" points="200,502 540,502 370,764"/>
  <polygon class="inner-line" points="225,514 515,514 370,738"/>
  <g text-anchor="middle">
    <circle cx="302" cy="561" r="5" fill="var(--pink)"/>
    <text class="body-text brand-name" x="375" y="570" font-size="28">Brightstep</text>
    <text class="body-text brand-sub" x="372" y="588" font-size="8">ACADEMY OF DANCE AND PERFORMING ARTS</text>
    <text class="body-text workshop-text" x="370" y="625" font-size="13">WEST END WORKSHOP</text>
    <text class="body-text workshop-text" x="370" y="643" font-size="12">Tuesday</text>
    <text class="body-text workshop-text" x="370" y="660" font-size="12">5 &amp; 6 April 2016</text>
    <text class="body-text workshop-text" x="370" y="677" font-size="12">8 – 16 years</text>
    <text class="body-text workshop-text" x="370" y="694" font-size="12">1-4pm</text>
  </g>

  <rect class="booking-box" x="56" y="690" width="176" height="74"/>
  <text class="body-text booking-label" x="144" y="708" font-size="12" text-anchor="middle">FOR BOOKING</text>
  <rect x="68" y="716" width="9" height="15" rx="2" fill="none" stroke="var(--blue)" stroke-width="2"/>
  <text class="body-text booking-phone" x="82" y="731" font-size="19">07700 900123</text>
  <text class="body-text booking-email" x="68" y="750" font-size="10">✉ hello@brightstepdance.co</text>
</svg>

</body>
</html>
```